Business Card Design for LeafCrest (Farming Devices)

We need Business Cards for our new Company based in Switzerland called "LeafCrest" We develop innovativ products for indoor and outdoor Farming for household and components for vertical farming. Our initial BloomNest gives people the possibility to grow their own food at home all year round. The design should communicate freshness, innovation, health.

```html
<!DOCTYPE html>
<html lang="en">
<head>
<meta charset="utf-8">
<title>LeafCrest Business Card</title>
<link href="https://fonts.googleapis.com/css2?family=Lato:wght@700&family=Open+Sans:wght@400;700&display=swap" rel="stylesheet">
<style>
  :root {
    --backdrop: #e4e4e4;
    --card-yellow: #fdea00;
    --card-green: #b0cc20;
    --leaf-green: #b2cc22;
    --leaf-soft: #d6dc10;
    --brand-green: #73a52d;
    --text-light: #ffffff;
  }
  * { box-sizing: border-box; margin: 0; padding: 0; }
  html, body {
    width: 1200px;
    height: 914px;
    overflow: hidden;
    background: var(--backdrop);
  }
  .stage {
    position: relative;
    width: 1200px;
    height: 914px;
  }
  .card {
    position: absolute;
    top: 162px;
    width: 337px;
    height: 590px;
    border-radius: 22px;
    overflow: hidden;
    box-shadow: 0 3px 4px rgba(0, 0, 0, 0.18);
  }
  .card-front {
    left: 240px;
    background: var(--card-yellow);
  }
  .card-back {
    left: 623px;
    background: var(--card-green);
    color: var(--text-light);
    font-family: "Open Sans", sans-serif;
  }
  .brand-mark {
    position: absolute;
    left: 50%;
    top: 200px;
    width: 48px;
    height: 48px;
    margin-left: -24px;
    border-radius: 50%;
    background: var(--brand-green);
  }
  .brand-name {
    position: absolute;
    left: 0;
    right: 0;
    top: 262px;
    text-align: center;
    font-family: "Lato", sans-serif;
    font-weight: 700;
    font-size: 62px;
    line-height: 1;
    color: var(--brand-green);
    letter-spacing: -0.5px;
  }
  .foliage {
    position: absolute;
    left: 0;
    right: 0;
    bottom: 0;
    height: 262px;
    background:
      radial-gradient(ellipse 60% 45% at 30% 75%, var(--leaf-green) 0%, transparent 70%),
      radial-gradient(ellipse 50% 50% at 80% 55%, var(--leaf-green) 0%, transparent 70%),
      linear-gradient(to bottom, var(--card-yellow) 0%, var(--leaf-soft) 35%, var(--leaf-green) 100%);
  }
  .holder-name {
    position: absolute;
    right: 44px;
    top: 67px;
    font-size: 21px;
    font-weight: 400;
    line-height: 1.2;
  }
  .holder-name strong { font-weight: 700; }
  .contact {
    position: absolute;
    right: 39px;
    top: 454px;
    text-align: right;
    font-size: 21px;
    line-height: 33px;
    font-style: normal;
  }
  .contact .phone { letter-spacing: 5px; margin-right: -5px; }
</style>
</head>
<body>
  <main class="stage">
    <section class="card card-front" aria-label="Card front">
      <span class="brand-mark" aria-hidden="true"></span>
      <h1 class="brand-name">LeafCrest</h1>
      <div class="foliage" role="img" aria-label="Pattern of drawn green leaves and sprouting stems along the bottom of the card"></div>
    </section>
    <section class="card card-back" aria-label="Card back">
      <p class="holder-name">Mara <strong>KELLER</strong></p>
      <address class="contact">
        <p class="phone">+123-45-9876543</p>
        <p class="email">Leafcrest@lcproject.com</p>
      </address>
    </section>
  </main>
</body>
</html>
```